Business Cards- The Estate at Brookhollow Golf Club

We would like our business cards to look more high-end. We are a wedding venue that has been in business for 60+ years. We like our logo and our colors - primarily green and a touch of gold/beige. The owner wants our business cards to look more special..

Target Market(s)

Brides who have already toured our venue

Industry/Entity Type

Wedding venue - mansion

Contact Information for Business Card

Name, email, physical address, phone number

Colors
00AB8E
00BBA5
67D7C9
C6EFE9
E9F9F6

Requirements
Must have
• I think we would like our cards to be so pretty that people will want to keep them and will remember the venue. The venue is historic (built in 1850) and beautiful.
Nice to have
• Could we put an image of the building on one side and the contact info on the other?
Should not have
• The color black

```html
<!DOCTYPE html>
<html lang="en">
<head>
<meta charset="utf-8">
<title>The Estate at Brookhollow Golf Club – Business Cards</title>
<link href="https://fonts.googleapis.com/css2?family=Montserrat:wght@400;500;600&display=swap" rel="stylesheet">
<style>
  :root {
    --bg: #e4e5e6;
    --card-cream: #f8f6f0;
    --green: #6b9b37;
    --green-line: #8cb25a;
    --beige: #cdb68e;
    --ink: #3f4a3c;
    --photo-dark: #24402a;
    --photo-light: #35603a;
  }
  * { margin: 0; padding: 0; box-sizing: border-box; }
  html, body { width: 1200px; height: 800px; overflow: hidden; }
  body {
    background: var(--bg);
    font-family: "Montserrat", Arial, sans-serif;
    display: flex;
    align-items: center;
    justify-content: center;
    gap: 40px;
  }
  .card {
    width: 540px;
    height: 309px;
    border-radius: 22px;
    position: relative;
    overflow: hidden;
    box-shadow: 0 10px 28px rgba(60, 70, 60, 0.18);
  }

  /* Contact side */
  .card-contact { background: var(--card-cream); }
  .brand {
    position: absolute;
    top: 44px;
    left: 200px;
    display: flex;
    align-items: center;
    gap: 10px;
  }
  .brand-mark {
    width: 16px; height: 16px;
    border-radius: 50%;
    background: var(--beige);
    flex: none;
  }
  .brand-name {
    font-size: 17px;
    font-weight: 600;
    color: var(--green);
    line-height: 1.25;
    max-width: 230px;
  }
  .divider {
    position: absolute;
    left: 40px; right: 32px;
    top: 178px;
    height: 1px;
    background: var(--green-line);
  }
  .person {
    position: absolute;
    left: 40px;
    top: 126px;
  }
  .person-name {
    font-size: 19px;
    font-weight: 600;
    letter-spacing: 1.5px;
    color: var(--green);
    text-transform: uppercase;
  }
  .person-title {
    font-size: 12px;
    color: var(--beige);
    margin-top: 3px;
  }
  .details {
    position: absolute;
    left: 40px;
    top: 194px;
    list-style: none;
    font-size: 12.5px;
    color: var(--ink);
  }
  .details li {
    display: flex;
    align-items: center;
    gap: 8px;
    margin-bottom: 6px;
  }
  .details svg { width: 12px; height: 12px; flex: none; }
  .address {
    position: absolute;
    right: 32px;
    top: 110px;
    text-align: right;
    font-size: 12.5px;
    line-height: 1.55;
    color: var(--ink);
  }
  .address .web { color: var(--green); }

  /* Photo side */
  .card-photo {
    background: linear-gradient(135deg, var(--photo-light) 0%, var(--photo-dark) 100%);
  }
  .photo-brand {
    position: absolute;
    top: 112px;
    left: 0; right: 0;
    display: flex;
    justify-content: center;
    align-items: center;
    gap: 12px;
  }
  .photo-brand .brand-name {
    font-size: 24px;
    max-width: none;
    color: var(--green-line);
  }
</style>
</head>
<body>
  <section class="card card-contact">
    <div class="brand">
      <span class="brand-mark"></span>
      <span class="brand-name">The Estate at Brookhollow Golf Club</span>
    </div>
    <div class="person">
      <div class="person-name">Helen Marlowe</div>
      <div class="person-title">President - Owner</div>
    </div>
    <div class="divider"></div>
    <ul class="details">
      <li>
        <svg viewBox="0 0 12 12" aria-hidden="true"><path d="M3 1 L5 3.5 L4 5 Q5 7 7 8 L8.5 7 L11 9 L9.5 11 Q4 10.5 1 3 Z" fill="var(--green)"/></svg>
        (410) 555-0142
      </li>
      <li>
        <svg viewBox="0 0 12 12" aria-hidden="true"><rect x="3" y="0.8" width="6" height="10.4" rx="1.2" fill="none" stroke="var(--green)" stroke-width="1.2"/></svg>
        (410) 555-0187
      </li>
      <li>
        <svg viewBox="0 0 12 12" aria-hidden="true"><rect x="0.8" y="2.5" width="10.4" height="7" rx="1" fill="var(--green)"/><path d="M1 3 L6 6.8 L11 3" fill="none" stroke="var(--card-cream)" stroke-width="1"/></svg>
        hmarlowe@brookhollowgolfclub.com
      </li>
    </ul>
    <div class="address">
      2240 Alder Lane<br>
      Fairhaven, MD 21090<br>
      <span class="web">BrookhollowGolfClub.com</span>
    </div>
  </section>

  <section class="card card-photo" role="img" aria-label="Photograph of an outdoor wedding ceremony set on a lawn: rows of white folding chairs either side of a paved aisle leading to a wooden arbor, in front of a tall row of evergreen trees under a blue sky with clouds">
    <div class="photo-brand">
      <span class="brand-mark"></span>
      <span class="brand-name">The Estate at Brookhollow Golf Club</span>
    </div>
  </section>
</body>
</html>
```